Coralith Partners's New Branding
Anything the customer sees, we want to update
Coralith Partners's New Branding -
Creative Brief
Professional
Dorian Pelk, MCP
Director of Technology
418 West Alder Road Morton, IL 61552
dorian.pelk@coralithpt.example
www.coralithpt.example
In addition to branding our business cards, we're also looking to brand: 1) folders - two pockets w/ a slotted area on the left pocket to insert a business card 2) brochures - 8.5"x11" tri-fold brochure 3) letterhead 4) envelopes 5) sales proposal cover letter - Our logo and name - Presented to: "Customer's name" - Presented by: "our sales person(s)" - Title of presentation - our web address 6) powerpoint 7) binders (including spline) 8) cd label - Company's name we're presenting cd to - our logo and name - title of content on cd
Quote: "Our business is sustaining yours" Please layout the quote so that if we put a QR code on the back of the card in the future, it won't look out of place.

```html
<!DOCTYPE html>
<html lang="en">
<head>
<meta charset="utf-8">
<title>Coralith Partners Stationery</title>
<link rel="stylesheet" href="https://fonts.googleapis.com/css2?family=Open+Sans:wght@400;600;700&display=swap">
<style>
  :root {
    --backdrop: #e4e5e4;
    --paper: #ffffff;
    --green-dark: #0d4f28;
    --green: #1f7a3a;
    --green-light: #4fa35a;
    --swoosh: #cdcfce;
    --ink: #3b3b3b;
    --ink-soft: #8a8a8a;
    --map-faint: #eef0ef;
  }
  * { box-sizing: border-box; margin: 0; padding: 0; }
  html, body { width: 1200px; height: 871px; overflow: hidden; }
  body {
    background: var(--backdrop);
    font-family: "Open Sans", Arial, sans-serif;
    color: var(--ink);
    position: relative;
  }
  .sheet {
    position: absolute;
    background: var(--paper);
    box-shadow: 0 3px 10px rgba(0,0,0,.18);
    overflow: hidden;
  }
  .brand { display: flex; align-items: center; gap: 6px; position: relative; z-index: 2; }
  .brand-dot {
    border-radius: 50%;
    background: radial-gradient(circle at 35% 35%, var(--green-light), var(--green-dark));
    flex: none;
  }
  .brand-name {
    font-weight: 700;
    color: var(--green-dark);
    letter-spacing: .06em;
    text-transform: uppercase;
    line-height: 1;
  }

  /* Letterhead */
  .letterhead { left: 34px; top: 173px; width: 333px; height: 448px; }
  .letterhead .brand { position: absolute; left: 22px; top: 24px; }
  .letterhead .brand-dot { width: 18px; height: 18px; }
  .letterhead .brand-name { font-size: 11px; }
  .letter-body { position: absolute; left: 22px; top: 70px; width: 289px; font-size: 5px; line-height: 1.6; color: var(--ink); }
  .recipient { margin-bottom: 10px; }
  .letter-date { position: absolute; right: 0; top: 38px; }
  .letter-body p { margin-bottom: 6px; }
  .signature-line { width: 70px; border-bottom: 1px solid var(--ink-soft); height: 14px; margin: 8px 0 3px; }
  .letter-map {
    position: absolute; left: 30px; top: 318px; width: 170px; height: 80px;
    background: radial-gradient(ellipse at center, var(--map-faint), rgba(238,240,239,0) 70%);
  }
  .letter-footer {
    position: absolute; left: 22px; right: 22px; bottom: 12px;
    font-size: 4.5px; color: var(--ink-soft); text-align: center;
    border-top: 1px solid var(--green); padding-top: 4px;
  }

  /* Presentation folder */
  .cover { left: 404px; top: 188px; width: 298px; height: 497px; }
  .cover .brand { position: absolute; left: 22px; top: 22px; }
  .cover .brand-dot { width: 20px; height: 20px; }
  .cover .brand-name { font-size: 13px; }
  .cover-swoosh { position: absolute; left: 0; top: 0; width: 100%; height: 100%; }
  .cover-map {
    position: absolute; left: 118px; top: 150px; width: 160px; height: 100px;
    background: radial-gradient(ellipse at 50% 45%, var(--green-light), var(--green) 45%, var(--green-dark) 80%);
    border-radius: 40% 45% 35% 40%;
  }
  .cover-tagline { position: absolute; left: 16px; top: 394px; font-size: 6.5px; color: var(--green); font-weight: 600; z-index: 2; }
  .cover-contact { position: absolute; left: 200px; top: 376px; font-size: 4.5px; line-height: 1.5; color: var(--ink-soft); z-index: 2; }

  /* Envelopes */
  .envelope-tall { left: 704px; top: 240px; width: 229px; height: 380px; }
  .envelope-wide { left: 505px; top: 620px; width: 327px; height: 170px; }
  .envelope-flap { position: absolute; left: 0; top: 0; width: 100%; }
  .flap-mark { position: absolute; left: 50%; transform: translateX(-50%); display: flex; flex-direction: column; align-items: center; gap: 2px; }
  .flap-mark .brand-dot { width: 10px; height: 10px; }
  .flap-mark .brand-name { font-size: 4px; color: var(--paper); }
  .envelope-tall .flap-mark { top: 8px; }
  .envelope-wide .flap-mark { top: 9px; }

  /* Business card */
  .business-card { left: 801px; top: 366px; width: 334px; height: 200px; }
  .business-card .brand { position: absolute; left: 18px; top: 22px; }
  .business-card .brand-dot { width: 15px; height: 15px; }
  .business-card .brand-name { font-size: 10px; }
  .card-swoosh { position: absolute; left: 0; top: 0; width: 100%; height: 100%; }
  .card-map {
    position: absolute; left: 178px; top: 36px; width: 140px; height: 90px;
    background: radial-gradient(ellipse at 50% 45%, var(--green-light), var(--green) 45%, var(--green-dark) 80%);
    border-radius: 40% 45% 35% 40%;
  }
  .card-details { position: absolute; left: 18px; bottom: 18px; font-size: 5px; line-height: 1.5; color: var(--ink-soft); z-index: 2; }
  .card-details .card-name { font-weight: 700; color: var(--green-dark); font-size: 6px; }
</style>
</head>
<body>

<section class="sheet letterhead" aria-label="Letterhead">
  <div class="brand"><span class="brand-dot"></span><span class="brand-name">Coralith Partners</span></div>
  <div class="letter-body">
    <span class="letter-date">Month Day, Year</span>
    <div class="recipient">Name<br>Title<br>Company Name<br>Street Address<br>City, State Zip</div>
    <p>Dear client, thank you for your continued trust in our team and the work we share.</p>
    <p>Our advisors review each plan with care so that your coverage keeps pace with your goals. We value clear answers, steady service and honest advice at every stage of growth.</p>
    <p>Please find the enclosed summary of options prepared for your review this season. Our staff will follow up within the week to answer questions and confirm next steps.</p>
    <p>We look forward to working with you.</p>
    <p>Sincerely,</p>
    <div class="signature-line"></div>
    <div>Dorian Pelk, MCP<br>Director of Technology</div>
  </div>
  <div class="letter-map" role="img" aria-label="Faint world map"></div>
  <div class="letter-footer">418 West Alder Road Morton, IL 61552 &nbsp;•&nbsp; (309) 555-0148 &nbsp;•&nbsp; www.coralithpt.example</div>
</section>

<section class="sheet cover" aria-label="Presentation folder">
  <svg class="cover-swoosh" viewBox="0 0 298 497" preserveAspectRatio="none" aria-hidden="true">
    <path d="M298 60 C190 62 36 140 28 250 C22 330 110 372 298 366 L298 352 C140 354 68 318 76 250 C88 160 210 92 298 86 Z" fill="var(--swoosh)"/>
  </svg>
  <div class="brand"><span class="brand-dot"></span><span class="brand-name">Coralith Partners</span></div>
  <div class="cover-map" role="img" aria-label="Green world map"></div>
  <p class="cover-tagline">Our business is sustaining yours</p>
  <div class="cover-contact">418 West Alder Road<br>Morton, IL 61552<br>(309) 555-0148<br>www.coralithpt.example</div>
</section>

<section class="sheet envelope-tall" aria-label="Envelope back">
  <svg class="envelope-flap" viewBox="0 0 229 40" aria-hidden="true">
    <defs><linearGradient id="flapTall" x1="0" y1="0" x2="0" y2="1"><stop offset="0" stop-color="#0d4f28"/><stop offset="1" stop-color="#2f8a45"/></linearGradient></defs>
    <path d="M0 0 H229 V30 L202 40 H27 L0 30 Z" fill="url(#flapTall)"/>
  </svg>
  <div class="flap-mark"><span class="brand-dot"></span><span class="brand-name">Coralith Partners</span></div>
</section>

<section class="sheet business-card" aria-label="Business card">
  <svg class="card-swoosh" viewBox="0 0 334 200" preserveAspectRatio="none" aria-hidden="true">
    <path d="M334 24 C240 26 150 72 150 124 C150 166 230 184 334 180 L334 170 C250 172 188 156 188 122 C188 84 260 50 334 46 Z" fill="var(--swoosh)"/>
  </svg>
  <div class="brand"><span class="brand-dot"></span><span class="brand-name">Coralith Partners</span></div>
  <div class="card-map" role="img" aria-label="Green world map"></div>
  <div class="card-details">
    <div class="card-name">Dorian Pelk, MCP</div>
    Director of Technology<br>418 West Alder Road Morton, IL 61552<br>dorian.pelk@coralithpt.example<br>www.coralithpt.example
  </div>
</section>

<section class="sheet envelope-wide" aria-label="Envelope back">
  <svg class="envelope-flap" viewBox="0 0 327 40" aria-hidden="true">
    <defs><linearGradient id="flapWide" x1="0" y1="0" x2="0" y2="1"><stop offset="0" stop-color="#0d4f28"/><stop offset="1" stop-color="#2f8a45"/></linearGradient></defs>
    <path d="M0 0 H327 V26 L163.5 40 L0 26 Z" fill="url(#flapWide)"/>
  </svg>
  <div class="flap-mark"><span class="brand-dot"></span><span class="brand-name">Coralith Partners</span></div>
</section>

</body>
</html>
```